A weight loss and fitness website design

I am into different types of modern weight loss techniques for people who are a little fatty and wish to be physically and mentally fit. Basically, the website is to teach people how to reduce weight using different methods such as diet, exercises, yoga and other forms. I would need an eye catching website which would make visitors want to come back. The will be also be different forms of exercises for a health and fit life. This said, my website is to have two categories of
1) weight loss techniques
2) exercise of fit and healthy living.
I prefer bright colors such as green, blue, yellow, and orange. Imagery should include before and after pictures of people suffering from obesity, people under going exercises.
Designers can get ideas and inspiration from the website fyrnexa.com which i was previously part of the team.
Target Market(s)
My target audience are people suffering from obesity, malnutrition and physical deficiency.
Industry/Entity Type
Fitness
Coding
Number of Pages Required
1 page
Look and feel

```html
<!DOCTYPE html>
<html lang="en">
<head>
<meta charset="utf-8">
<title>Plumora — Fitness &amp; Weight Loss</title>
<link href="https://fonts.googleapis.com/css2?family=Raleway:ital,wght@0,400;0,500;0,600;1,500&family=Open+Sans:wght@400;600&display=swap" rel="stylesheet">
<style>
:root{
  --blue:#1e8fd6;
  --sky:#2eb3e8;
  --navy:#1d3d72;
  --green:#8cc63f;
  --orange:#f7931e;
  --sun-yellow:#ffd54a;
  --text:#555c66;
  --muted:#8a9099;
  --rule:#e3e6ea;
  --grey-bg:#eef0f1;
  --footer:#0e1b33;
  --white:#fff;
}
*{box-sizing:border-box;margin:0;padding:0}
html,body{width:1200px;height:4839px;overflow:hidden}
body{font-family:"Open Sans",Arial,sans-serif;color:var(--text);background:var(--white);position:relative;font-size:13px;line-height:1.6}
.abs{position:absolute}
.ph{position:absolute}
h2,h3,h4{font-family:"Raleway",Arial,sans-serif;font-weight:500;color:#333}
.section-title{font-size:25px;letter-spacing:.5px;text-transform:uppercase;color:#2f3338}
.copy{font-size:12.5px;line-height:1.75;color:var(--muted)}
.btn-green{display:inline-block;background:var(--green);color:#fff;font-size:12px;padding:4px 14px;border-radius:2px}

/* nav */
.site-nav{top:0;left:0;width:1200px;height:80px;border-bottom:1px solid var(--rule);display:flex;justify-content:center}
.nav-item{width:108px;text-align:center;font-size:12px;color:#555;padding-top:14px}
.nav-item .ico{display:block;width:22px;height:22px;margin:0 auto 6px}
.nav-item.active{background:var(--blue);color:#fff;border-radius:0 0 54px 54px;height:84px}
/* brand */
.brand{top:150px;left:0;width:1200px;display:flex;justify-content:center;align-items:center;gap:18px}
.brand-mark{width:110px;height:110px;border-radius:50%;background:var(--blue)}
.brand-name{font-family:"Raleway",sans-serif;font-size:78px;font-weight:500;color:var(--green)}
/* subscribe */
.subscribe{top:387px;left:0;width:1200px;height:82px;background:#f5f6f7}
.subscribe-lead{left:80px;top:18px;width:280px;font-family:"Raleway",sans-serif;font-style:italic;font-weight:500;color:var(--blue);font-size:14px;line-height:1.45}
.email-label{left:370px;top:29px;font-size:12px;color:#333}
.email-input{left:475px;top:26px;width:270px;height:30px;background:#fff;border:1px solid #ccd}
.sub-btn{left:745px;top:26px;width:100px;height:30px;background:var(--blue);color:#fff;font-size:12px;text-align:center;line-height:30px}
.social{left:905px;top:22px;display:flex;gap:10px}
.social span{width:36px;height:36px;border-radius:50%;background:var(--blue)}
/* hero */
.crowd-strip{top:469px;left:0;width:1200px;height:66px;background:linear-gradient(#fff,#f3efe6)}
.hero{top:535px;left:0;width:1200px;height:546px;background:linear-gradient(180deg,#f2a33c 0%,#f7c35b 35%,#e98a26 60%,#6a4a2c 100%)}
.hero-text{left:520px;top:210px;font-family:"Raleway",sans-serif;font-weight:500;font-size:38px;line-height:1.25;color:#1ab0e8}
.hero-text .alt{color:var(--sun-yellow)}
.hero-btn{left:575px;top:335px;width:210px;height:48px;background:var(--orange);color:#fff;font-family:"Raleway",sans-serif;font-size:20px;text-align:center;line-height:48px}
/* keep fit */
.fit{top:1081px;left:0;width:1200px;height:500px;background:linear-gradient(180deg,#fff 0%,#fff 40%,#f2f7fb 100%)}
.fit .section-title{position:absolute;top:58px;width:100%;text-align:center;color:var(--navy)}
.fit .copy{position:absolute;top:128px;left:110px;width:980px;text-align:center;color:#666}
.card{position:absolute;top:209px;height:204px;background:linear-gradient(90deg,#8b8f97 0%,#7aa9c9 38%,#29a3dd 45%,#1b8fd0 100%);border:3px solid #fff;box-shadow:0 2px 6px rgba(0,0,0,.15)}
.card h3{position:absolute;right:14px;top:20px;color:#fff;font-size:30px;font-weight:400;text-align:right;line-height:1.05}
.card p{position:absolute;right:14px;top:74px;width:45%;color:#e6f3fb;font-size:10px;line-height:1.4}
.card.two-line p{top:100px}
.card .btn-green{position:absolute;right:20px;bottom:18px;font-size:10px}
/* calendar */
.cal-sec{top:1581px;left:0;width:1200px;height:693px;border-top:1px solid var(--rule)}
.runner{left:70px;top:80px;width:300px;height:460px;background:linear-gradient(160deg,#7a4a30,#b22a2a 55%,#d7d7d7)}
.cal-sec .section-title,.cal-sec .copy{position:absolute;left:610px;width:480px}
.cal-sec .section-title{top:58px}
.cal-sec .copy{top:110px}
.calendar{left:610px;top:290px;width:475px;height:355px;background:var(--grey-bg);padding:30px 28px}
.cal-head{font-family:"Raleway",sans-serif;font-size:40px}
.cal-head .y{color:var(--orange)} .cal-head .m{color:var(--green)}
.fruit{right:30px;top:25px;width:110px;height:60px;background:linear-gradient(90deg,#c8323a,#4a7a2c)}
.cal-grid{margin-top:10px;width:420px;border-collapse:collapse;font-size:15px}
.cal-grid th{font-weight:600;color:#333;text-align:left;padding:6px 4px;border-bottom:1px solid #ccc}
.cal-grid td{padding:9px 4px;color:#444;border-bottom:1px solid #e0e0e0}
.cal-grid td.sun{color:#d9363e}
/* progress */
.progress{top:2274px;left:0;width:1200px;height:678px;background:var(--grey-bg)}
.progress .section-title{position:absolute;left:80px;top:48px;font-size:22px}
.progress .copy{position:absolute;left:80px;top:90px;width:470px}
.chart{left:80px;top:270px;width:470px;height:360px;background:linear-gradient(135deg,#ffffff 0%,#f6e3e3 45%,#f3d27a 100%)}
.athlete{left:690px;top:25px;width:420px;height:600px;background:linear-gradient(170deg,#e9ecef,#c9b7a8 40%,#5a5f66 75%,#e9ecef)}
/* daily */
.daily{top:2952px;left:0;width:1200px;height:661px}
.couple{left:150px;top:25px;width:285px;height:625px;background:linear-gradient(180deg,#fff,#b08a6e 30%,#3a3a3a 65%,#e3c84a 95%)}
.daily .section-title,.daily .copy{position:absolute;left:610px;width:480px}
.daily .section-title{top:58px;font-size:22px}
.daily .copy{top:95px}
.notes{left:615px;top:275px;width:470px;height:362px;background:#2e5e34}
/* diet */
.diet{top:3613px;left:0;width:1200px;height:484px;background:linear-gradient(180deg,#eaf4fb,#f6fafd)}
.food{left:80px;top:75px;width:480px;height:340px;background:linear-gradient(120deg,#f1f1f1,#e99a6b 35%,#f5f5f5 55%,#3d7a3a 80%,#8a3b2c)}
.diet h2{position:absolute;left:625px;top:70px;font-size:32px;color:#333}
.diet .copy{position:absolute;left:625px;width:470px}
.diet .c1{top:125px} .diet .c2{top:215px}
.diet-btns{left:625px;top:290px;display:flex;gap:12px}
/* testimonial */
.testi{top:4097px;left:0;width:1200px;height:355px}
.testi .section-title{position:absolute;left:80px;top:50px;font-size:27px;color:var(--navy)}
.arrows{left:535px;top:52px;color:var(--blue);font-size:26px;font-family:"Raleway",sans-serif;letter-spacing:6px}
.quote{left:80px;top:95px;width:490px;height:145px;border:2px solid #444;border-radius:6px;padding:14px 18px;font-size:11.5px;color:#555;line-height:1.6}
.quote b{display:block;margin-top:10px;color:#333;font-size:11px}
.quote small{font-size:10px;color:#888}
.group{left:580px;top:33px;width:535px;height:322px;background:linear-gradient(180deg,#fff,#b7d7ea 35%,#e49bb6 55%,#8a8f96 100%)}
/* footer */
.footer{top:4452px;left:0;width:1200px;height:355px;background:var(--footer);color:#c9d2df}
.footer h4{position:absolute;top:22px;color:#fff;font-size:21px;font-weight:500}
.event{left:80px;width:420px;display:flex;gap:14px}
.event .thumb{flex:none;width:110px;height:80px;background:linear-gradient(135deg,#5a3b2a,#b67a4f)}
.event p{font-size:10.5px;line-height:1.5;color:#c9d2df}
.event p b{color:#fff;font-weight:600}
.addr{left:530px;top:68px;width:260px;font-size:11px;line-height:1.6}
.addr div{display:flex;gap:8px;margin-bottom:8px}
.addr svg{flex:none;margin-top:3px}
.map{left:530px;top:205px;width:230px;height:100px;background:linear-gradient(135deg,#e9e4d8,#cfd8c6)}
.news-input{left:840px;width:280px;height:26px;background:#fff}
.news-btn{left:840px;top:140px;width:82px;height:28px;background:var(--blue);color:#fff;font-size:11px;text-align:center;line-height:28px}
.f-social{left:840px;top:185px;display:flex;gap:6px}
.f-social span{width:30px;height:30px;background:var(--sky)}
.copyright{top:4807px;left:0;width:1200px;height:32px;background:var(--green);color:#fff;text-align:center;font-size:11px;line-height:32px}
</style>
</head>
<body>

<nav class="site-nav abs">
  <div class="nav-item active"><svg class="ico" viewBox="0 0 22 22"><path d="M2 11 11 3l9 8M5 9v10h12V9" fill="none" stroke="#fff" stroke-width="2"/></svg>Home</div>
  <div class="nav-item"><svg class="ico" viewBox="0 0 22 22"><circle cx="11" cy="7" r="4" fill="#8cc63f"/><path d="M3 20c1-6 15-6 16 0z" fill="#8cc63f"/></svg>About</div>
  <div class="nav-item"><svg class="ico" viewBox="0 0 22 22"><rect x="2" y="9" width="18" height="4" fill="#8cc63f"/><rect x="3" y="5" width="3" height="12" fill="#8cc63f"/><rect x="16" y="5" width="3" height="12" fill="#8cc63f"/></svg>Work Out With Me</div>
  <div class="nav-item"><svg class="ico" viewBox="0 0 22 22"><path d="M6 2v18M3 2v6h6V2M16 2c-3 3-3 7 0 9v9" fill="none" stroke="#8cc63f" stroke-width="2"/></svg>Recipes</div>
  <div class="nav-item"><svg class="ico" viewBox="0 0 22 22"><circle cx="13" cy="4" r="2.5" fill="#8cc63f"/><path d="M6 20l4-7 3 3 2 4M8 10l4-3 4 4" fill="none" stroke="#8cc63f" stroke-width="2"/></svg>Fitness</div>
  <div class="nav-item"><svg class="ico" viewBox="0 0 22 22"><circle cx="8" cy="8" r="3" fill="#8cc63f"/><circle cx="15" cy="8" r="3" fill="#8cc63f"/><path d="M2 19c1-5 17-5 18 0z" fill="#8cc63f"/></svg>Sponsor</div>
  <div class="nav-item"><svg class="ico" viewBox="0 0 22 22"><path d="M11 19S2 13 2 7.5A4.5 4.5 0 0 1 11 5a4.5 4.5 0 0 1 9 2.5C20 13 11 19 11 19z" fill="#8cc63f"/></svg>Family</div>
  <div class="nav-item"><svg class="ico" viewBox="0 0 22 22"><path d="M3 4h16v11H9l-5 4v-4H3z" fill="#8cc63f"/></svg>Friends</div>
  <div class="nav-item"><svg class="ico" viewBox="0 0 22 22"><rect x="3" y="4" width="16" height="16" fill="none" stroke="#8cc63f" stroke-width="2"/><path d="M3 9h16M7 2v4M15 2v4" stroke="#8cc63f" stroke-width="2"/></svg>Book</div>
</nav>

<header class="brand abs">
  <span class="brand-mark"></span>
  <span class="brand-name">Plumora</span>
</header>

<section class="subscribe abs">
  <p class="subscribe-lead abs">Subscribe for famous Workouts Recipes and Fitness calendars</p>
  <span class="email-label abs">Email Address <span style="color:#d33">*</span></span>
  <span class="email-input abs"></span>
  <span class="sub-btn abs">Subscribe</span>
  <div class="social abs"><span></span><span></span><span></span><span></span><span></span></div>
</section>

<div class="crowd-strip ph" role="img" aria-label="Row of small drawn figures doing exercises"></div>

<section class="hero abs">
  <div class="ph" style="inset:0" role="img" aria-label="Two people meditating on a beach at sunset, arms raised"></div>
  <h1 class="hero-text abs">Fitness Is Not A Destination<br><span class="alt">It Is A Way Of Life.</span></h1>
  <span class="hero-btn abs">Sign Up Now</span>
</section>

<section class="fit abs">
  <h2 class="section-title">Keep Your Body Fit &amp; Healthy</h2>
  <p class="copy">Small daily habits add up to lasting change. Move a little more each day, eat fresh whole foods, sleep well and drink plenty of water. Our plans guide you step by step with simple workouts, easy recipes and steady support, so you can lose weight, gain strength and feel better in body and mind.</p>
  <article class="card" style="left:80px;width:295px" role="img" aria-label="Man lifting a dumbbell"><h3>Exercises</h3><p>Short routines for every level that build strength and burn fat at home.</p><span class="btn-green">More Details</span></article>
  <article class="card two-line" style="left:435px;width:330px" role="img" aria-label="Hands holding a red heart"><h3>Improve Health &amp;<br>Wellbeing</h3><p>Calm the mind and lift your mood with breathing, yoga and rest.</p><span class="btn-green">More Details</span></article>
  <article class="card" style="left:790px;width:330px" role="img" aria-label="Toned stomach muscles"><h3>Weightloss</h3><p>Proven methods to shed weight safely and keep it off for good.</p><span class="btn-green">More Details</span></article>
</section>

<section class="cal-sec abs">
  <div class="runner ph" role="img" aria-label="Athlete sprinting in red shorts"></div>
  <h2 class="section-title">Customizable Workout Calendar</h2>
  <p class="copy">Plan your week your way. Pick the days you train, choose the type of session and set the length that suits you. The calendar sends gentle reminders, marks every finished workout and shifts sessions when life gets busy, so you always know what comes next and never lose your rhythm.</p>
  <div class="calendar abs">
    <div class="cal-head"><span class="y">2016</span> <span class="m">MAY</span></div>
    <div class="fruit ph" role="img" aria-label="Cherries and a fig"></div>
    <table class="cal-grid">
      <tr><th>SUN</th><th>MON</th><th>TUE</th><th>WED</th><th>THURS</th><th>FRI</th><th>SAT</th></tr>
      <tr><td class="sun">1</td><td>2</td><td>3</td><td>4</td><td>5</td><td>6</td><td>7</td></tr>
      <tr><td class="sun">8</td><td>9</td><td>10</td><td>11</td><td>12</td><td>13</td><td>14</td></tr>
      <tr><td class="sun">15</td><td>16</td><td>17</td><td>18</td><td>19</td><td>20</td><td>21</td></tr>
      <tr><td class="sun">22</td><td>23</td><td>24</td><td>25</td><td>26</td><td>27</td><td>28</td></tr>
      <tr><td class="sun">29</td><td>30</td><td>31</td><td></td><td></td><td></td><td></td></tr>
    </table>
  </div>
</section>

<section class="progress abs">
  <h2 class="section-title">Progress Tracking</h2>
  <p class="copy">Watch your results grow week by week. Log your weight, waist size and workouts in one place and see clear charts of your progress. Set small goals, celebrate each milestone and spot what works best for you. Seeing real change keeps you motivated and helps you stay on track for the long run.</p>
  <div class="chart ph" role="img" aria-label="Illustration of a pencil drawing a rising progress line on graph paper"></div>
  <div class="athlete ph" role="img" aria-label="Woman in sportswear mid-jump"></div>
</section>

<section class="daily abs">
  <div class="couple ph" role="img" aria-label="Fit couple holding dumbbells back to back"></div>
  <h2 class="section-title">Daily Workout Programs</h2>
  <p class="copy">Fresh sessions every day, from gentle walks and stretching to strength circuits and cardio. Each program explains every move, suits beginners and grows harder as you get fitter.</p>
  <div class="notes ph" role="img" aria-label="Sticky notes on a board reading good food, good workout, good rest, good health"></div>
</section>

<section class="diet abs">
  <div class="food ph" role="img" aria-label="Salmon, eggs, milk, greens and beans"></div>
  <h2>Diet Plans</h2>
  <p class="copy c1">Eat well without feeling hungry. Our meal plans balance protein, fresh vegetables and whole grains, with simple recipes and shopping lists for every week of your journey.</p>
  <p class="copy c2">Choose a plan that fits your tastes and daily routine, and swap meals whenever you like.</p>
  <div class="diet-btns abs"><span class="btn-green">For Men</span><span class="btn-green">For Women</span><span class="btn-green">More Details</span></div>
</section>

<section class="testi abs">
  <h2 class="section-title">Testimonial</h2>
  <span class="arrows abs">‹ ›</span>
  <blockquote class="quote abs">The plans were easy to follow and the daily workouts fit around my job. I lost weight steadily, sleep better and feel more confident than I have in years. The support kept me going.<b>Aled Fenwick</b><small>Customer</small></blockquote>
  <div class="group ph" role="img" aria-label="Group of smiling people of different ages in sportswear"></div>
</section>

<footer class="footer abs">
  <h4 style="left:80px">Event Information</h4>
  <div class="event abs" style="top:75px"><span class="thumb" role="img" aria-label="Muscular athlete"></span><p><b>Morning boot camp in the park</b><br>Join our group session for all levels. Bring water, a mat and a friend to train with.</p></div>
  <div class="event abs" style="top:185px"><span class="thumb" role="img" aria-label="Muscular athlete"></span><p><b>Healthy cooking evening class</b><br>Learn quick, tasty meals that help you lose weight and keep your energy high.</p></div>
  <h4 style="left:530px">Our Address</h4>
  <div class="addr abs">
    <div><svg width="10" height="12" viewBox="0 0 10 12"><path d="M5 0a4 4 0 0 1 4 4c0 3-4 8-4 8S1 7 1 4a4 4 0 0 1 4-4z" fill="#c9d2df"/></svg><span>Plumora Unit 4, Larkmoor Yard, Eastfield, Northvale</span></div>
    <div><svg width="10" height="12" viewBox="0 0 10 12"><path d="M2 0h3l1 3-2 1q1 3 3 4l1-2 3 1v3q-7 1-10-9z" fill="#c9d2df"/></svg><span>0800 555 0147</span></div>
    <div><svg width="12" height="9" viewBox="0 0 12 9"><rect width="12" height="9" fill="#c9d2df"/><path d="M0 0l6 5 6-5" fill="none" stroke="#0e1b33"/></svg><span>hello@plumora-fit.example</span></div>
  </div>
  <div class="map ph" role="img" aria-label="Street map of the studio location"></div>
  <h4 style="left:840px">Our Newsletter</h4>
  <span class="news-input abs" style="top:68px"></span>
  <span class="news-input abs" style="top:102px"></span>
  <span class="news-btn abs">SIGN UP</span>
  <div class="f-social abs"><span></span><span></span><span></span><span></span><span></span><span></span><span></span><span></span></div>
</footer>
<div class="copyright abs">Copyright 2016 @plumora-fit.example. All rights are reserved</div>

</body>
</html>
```